COMING SOON PAGE for BEAUTY WEBSITE

Looking for a very beautiful, high end coming soon page for the site, www.glowparlorqz.com

looking for the site to have a bit of text and fade thru a few images -- beautiful fonts, modern airy feel.

Text on page:

it doesn't have to be complicated
glowparlorqz.com coming soon
beauty, simplified.

Please use all lowercase and place the logo somewhere on the page...logo attached and images attached -- happy to provide more images if necessary

You can play with images, zoom in, dont need to use whole image, etc....modern, classy, airy.

thanks.

Target Market(s)

35-60 year old women, modern, elegant, look conscious

Number of Pages Required

1 page

Font styles to use
Sans Serif

Requirements
Must have
• Images fade from one to other slowly and elegantly -- or slide, etc..some sort of elegant transition
• Opaque, airy feel
• logo must be present and easy to identify
Should not have
• NO SOUND
• NO SCRIPT TEXT

```html
<!DOCTYPE html>
<html lang="en">
<head>
<meta charset="utf-8">
<title>glowparlorqz — coming soon</title>
<link rel="stylesheet" href="https://fonts.googleapis.com/css2?family=Poiret+One&family=Roboto+Condensed:wght@300&family=Arimo:wght@400&family=Barlow+Semi+Condensed:wght@400;500&display=swap">
<style>
  :root {
    --ink: #1e1b1c;
    --muted: #6f6a6c;
    --frame: rgba(255, 255, 255, 0.32);
    --slide-deep: #2a4d5c;
    --slide-mid: #3f6776;
    --slide-light: #5b7f8a;
    --pink: #e5648f;
    --pink-edge: #c94a76;
    --white: #ffffff;
    --soft-white: rgba(255, 255, 255, 0.82);
  }
  * { box-sizing: border-box; margin: 0; padding: 0; }
  html, body { width: 1200px; height: 674px; overflow: hidden; }
  body { position: relative; background: #e9e4e6; }

  .backdrop {
    position: absolute; inset: 0;
    background:
      radial-gradient(ellipse 320px 260px at 120px 560px, rgba(214,110,130,0.55), transparent 70%),
      radial-gradient(ellipse 300px 240px at 1120px 560px, rgba(120,240,240,0.75), transparent 70%),
      radial-gradient(ellipse 280px 200px at 1000px 120px, rgba(236,170,140,0.55), transparent 70%),
      radial-gradient(ellipse 260px 220px at 300px 120px, rgba(200,200,240,0.6), transparent 70%),
      linear-gradient(135deg, #d9cfd4 0%, #efe9ea 45%, #e6dcd8 70%, #cfe6e6 100%);
  }
  .frame {
    position: absolute; left: 19px; top: 19px; width: 1161px; height: 634px;
    background: var(--frame);
  }

  .brand {
    position: absolute; left: 57px; top: 44px;
    font-family: "Poiret One", sans-serif; font-weight: 400;
    font-size: 56px; line-height: 1; color: var(--ink); letter-spacing: 0.5px;
  }

  .slider {
    position: absolute; left: 271px; top: 178px; width: 657px; height: 335px;
    box-shadow: 0 3px 8px rgba(0,0,0,0.28);
    overflow: hidden;
  }
  .slide-photo {
    position: absolute; inset: 0;
    background:
      radial-gradient(ellipse 200px 220px at 420px 300px, rgba(140,120,100,0.45), transparent 70%),
      linear-gradient(160deg, var(--slide-deep) 0%, var(--slide-mid) 55%, var(--slide-light) 100%);
  }
  .slide-arrow { position: absolute; top: 142px; }
  .slide-arrow.prev { left: 24px; }
  .slide-arrow.next { right: 22px; }

  .slide-copy { position: absolute; left: 91px; top: 94px; color: var(--white); }
  .slide-title {
    font-family: "Roboto Condensed", sans-serif; font-weight: 300;
    font-size: 37px; line-height: 1; letter-spacing: -0.3px;
  }
  .slide-text {
    margin-top: 14px;
    font-family: "Arimo", sans-serif; font-size: 14px; line-height: 21px;
    color: var(--soft-white);
  }

  .signup { position: absolute; left: 91px; top: 201px; display: flex; gap: 16px; }
  .signup-field, .signup-button {
    height: 45px; background: var(--pink);
    border: 2px solid var(--pink-edge); border-radius: 4px;
    font-family: "Arimo", sans-serif; color: rgba(255,255,255,0.55);
    display: flex; align-items: center;
  }
  .signup-field { width: 339px; padding-left: 20px; font-size: 21px; }
  .signup-button { width: 47px; justify-content: center; font-size: 19px; color: var(--white); }

  .slide-dots { position: absolute; top: 297px; left: 301px; display: flex; gap: 11px; }
  .slide-dots span { width: 9px; height: 9px; border-radius: 50%; background: var(--white); }
  .slide-dots span.inactive { background: rgba(255,255,255,0.4); }

  .footer {
    position: absolute; left: 0; width: 1200px; top: 620px; text-align: center;
    font-family: "Barlow Semi Condensed", sans-serif; font-size: 17px; letter-spacing: 0.2px;
  }
  .footer-name { color: var(--ink); font-weight: 500; margin-right: 6px; }
  .footer-address { color: var(--muted); font-weight: 400; }
</style>
</head>
<body>
  <div class="backdrop" role="img" aria-label="soft pastel photograph of flowing hair in pink, peach and aqua tones"></div>
  <div class="frame"></div>

  <div class="brand">glowparlorqz</div>

  <section class="slider">
    <div class="slide-photo" role="img" aria-label="photograph of a woman with flowing hair against a starry teal sky"></div>

    <svg class="slide-arrow prev" width="24" height="58" viewBox="0 0 24 58" aria-hidden="true">
      <polyline points="23,1 1,29 23,57" fill="none" stroke="rgba(255,255,255,0.7)" stroke-width="1.3"/>
    </svg>
    <svg class="slide-arrow next" width="24" height="58" viewBox="0 0 24 58" aria-hidden="true">
      <polyline points="1,1 23,29 1,57" fill="none" stroke="rgba(255,255,255,0.7)" stroke-width="1.3"/>
    </svg>

    <div class="slide-copy">
      <h1 class="slide-title">beauty simplified</h1>
      <p class="slide-text">please check back soon our web site is currently<br>under development due to be finished as soon as possible</p>
    </div>

    <div class="signup">
      <div class="signup-field">enter your email address</div>
      <div class="signup-button">go</div>
    </div>

    <div class="slide-dots">
      <span></span><span class="inactive"></span><span></span><span></span>
    </div>
  </section>

  <footer class="footer">
    <span class="footer-name">glowparlorqz</span>
    <span class="footer-address">address line 1, city, area postal code</span>
  </footer>
</body>
</html>
```